Family Ranch with a hobby vineyard needs 2 wine labels for our first harvest

Design 2 wine labels (front and back) with the Brindor Ranch logo.
Label 1:
Sauvignon Blanc
Alc. 12.5% by Vol.
Palos Verdes Peninsula - add as the region
Year 2022
Label 2:
Cabernet Sauvignon
Alc. 13.5% by Vol.
Year 2022
For the back label design:
GOVERNMENT WARNING: (1) According to the Surgeon General, women
should not drink alcoholic beverages during pregnancy because of the risk of
birth defects. (2) Consumption of alcoholic beverages impairs your ability to
drive a car or operate machinery, and may cause health problems.
Contains Sulfates.
750ML
I just received the bottles and have attached a picture.
Look and feel
Each slider illustrates characteristics of the customer's brand and the style your logo design should communicate.

```html
<!DOCTYPE html>
<html lang="en">
<head>
<meta charset="utf-8">
<title>Brindor Ranch – Cabernet Sauvignon Labels</title>
<link href="https://fonts.googleapis.com/css2?family=Montserrat:wght@300;400;500;700&display=swap" rel="stylesheet">
<style>
  :root {
    --page: #ffffff;
    --ink: #141414;
    --band-top: #252525;
    --band-bottom: #333333;
    --cream: #e6e0db;
    --text-dark: #1c1a1a;
    --muted: #6e6464;
    --dot: #9c9494;
  }
  * { margin: 0; padding: 0; box-sizing: border-box; }
  html, body {
    width: 1200px; height: 1200px; overflow: hidden;
    background: var(--page);
    font-family: "Montserrat", sans-serif;
  }
  .canvas { position: relative; width: 1200px; height: 1200px; }

  /* Front label */
  .front-label {
    position: absolute; left: 173px; top: 239px;
    width: 401px; height: 729px;
    background: var(--ink);
    color: var(--cream);
  }
  .brand-name {
    position: absolute; left: 0; right: 0; text-align: center;
    font-weight: 500; color: var(--cream);
    line-height: 1;
  }
  .front-label .brand-name { top: 50px; }
  .brand-name .word-main { display: block; font-size: 33px; letter-spacing: 0.02em; }
  .brand-name .word-sub { display: block; font-size: 13px; letter-spacing: 0.45em; margin-top: 6px; padding-left: 0.45em; }

  .hero-mark {
    position: absolute; left: 50%; top: 196px; transform: translateX(-50%);
    width: 260px; height: 260px; border-radius: 50%;
    border: 22px solid var(--cream);
    display: flex; align-items: center; justify-content: center;
  }
  .hero-name {
    font-size: 30px; font-weight: 500; letter-spacing: 0.04em;
    color: var(--cream);
  }

  .varietal-band {
    position: absolute; left: 0; right: 0; bottom: 0; height: 171px;
    background: linear-gradient(180deg, var(--band-top), var(--band-bottom));
  }
  .varietal-band::before {
    content: ""; position: absolute; left: 0; right: 0; top: -5px; height: 10px;
    background: radial-gradient(circle at 50% 50%, var(--band-top) 4.5px, transparent 5px) 0 0 / 12px 10px repeat-x;
  }
  .varietal {
    position: absolute; left: 13px; right: 13px; top: 35px;
    font-size: 24px; font-weight: 700; letter-spacing: 0.12em;
    text-align: center; color: #f2efec; white-space: nowrap;
  }
  .dotted-rule {
    position: absolute; height: 3px;
    background: radial-gradient(circle, var(--dot) 1.2px, transparent 1.5px) 0 0 / 8px 3px repeat-x;
  }
  .varietal-band .dotted-rule { left: 22px; right: 36px; top: 74px; }
  .region {
    position: absolute; left: 8px; right: 8px; top: 86px;
    font-size: 22px; font-weight: 300; letter-spacing: 0.115em;
    text-align: center; color: #f2efec; white-space: nowrap;
  }
  .vintage-row {
    position: absolute; left: 13px; right: 18px; top: 126px;
    display: flex; justify-content: space-between;
    font-size: 19px; color: #f2efec;
  }
  .vintage { font-weight: 400; }
  .abv { font-weight: 700; letter-spacing: 0.02em; }

  /* Back label */
  .back-label {
    position: absolute; left: 631px; top: 426px;
    width: 412px; height: 542px;
    background: var(--ink);
  }
  .back-label .brand-mark {
    position: absolute; left: 50%; top: 30px; transform: translateX(-50%);
    width: 40px; height: 40px; border-radius: 50%;
    border: 4px solid var(--cream);
  }
  .back-label .brand-name { top: 92px; }
  .back-label .word-main { font-size: 21px; }
  .back-label .word-sub {
    font-size: 9px; letter-spacing: 0.4em; margin-top: 3px;
    display: flex; align-items: center; justify-content: center; gap: 5px; padding-left: 0;
  }
  .back-label .word-sub::before,
  .back-label .word-sub::after {
    content: ""; width: 24px; height: 1.5px; background: var(--cream);
  }

  .warning-panel {
    position: absolute; left: 23px; top: 155px;
    width: 365px; height: 338px;
    background: var(--cream); color: var(--text-dark);
  }
  .warning-panel::before,
  .warning-panel::after {
    content: ""; position: absolute; top: 0; bottom: 0; width: 4px;
  }
  .warning-panel::before {
    left: 0;
    background: radial-gradient(circle at 0 50%, var(--ink) 2.6px, transparent 3px) 0 0 / 4px 8px repeat-y;
  }
  .warning-panel::after {
    right: 0;
    background: radial-gradient(circle at 100% 50%, var(--ink) 2.6px, transparent 3px) 0 0 / 4px 8px repeat-y;
  }
  .warning-title {
    position: absolute; left: 28px; top: 21px;
    font-size: 17.5px; font-weight: 700; letter-spacing: 0.18em; white-space: nowrap;
  }
  .warning-text {
    position: absolute; left: 31px; width: 320px;
    font-size: 14.5px; font-weight: 400; letter-spacing: 0.12em; line-height: 20px;
    white-space: nowrap;
  }
  .warning-text.first { top: 52px; }
  .warning-text.second { top: 169px; }
  .warning-panel .dotted-rule { left: 31px; right: 28px; }
  .warning-panel .rule-one { top: 160px; }
  .warning-panel .rule-two { top: 287px; }
  .panel-footer {
    position: absolute; left: 31px; right: 29px; top: 297px;
    display: flex; justify-content: space-between;
    font-size: 16px; color: var(--muted); letter-spacing: 0.02em;
  }
  .volume { font-weight: 700; }
  .allergen { font-weight: 400; }
</style>
</head>
<body>
<main class="canvas">
  <section class="front-label">
    <div class="brand-name">
      <span class="word-main">BRINDOR</span>
      <span class="word-sub">RANCH</span>
    </div>
    <div class="hero-mark">
      <span class="hero-name">BRINDOR</span>
    </div>
    <div class="varietal-band">
      <h1 class="varietal">CABERNET SAUVIGNON</h1>
      <div class="dotted-rule"></div>
      <p class="region">PALOS VERDES PENINSULA</p>
      <div class="vintage-row">
        <span class="vintage">YEAR 2022</span>
        <span class="abv">13.5% VOL</span>
      </div>
    </div>
  </section>

  <section class="back-label">
    <div class="brand-mark"></div>
    <div class="brand-name">
      <span class="word-main">BRINDOR</span>
      <span class="word-sub">RANCH</span>
    </div>
    <div class="warning-panel">
      <h2 class="warning-title">GOVERNMENT WARNING:</h2>
      <p class="warning-text first">According to the Surgeon<br>General, women should not<br>drink alcoholic beverages during<br>pregnancy because of the risk<br>of birth defects.</p>
      <div class="dotted-rule rule-one"></div>
      <p class="warning-text second">Consumption of alcoholic<br>beverages impairs your ability<br>to drive a car or operate<br>machinery, and may cause<br>health problems.</p>
      <div class="dotted-rule rule-two"></div>
      <div class="panel-footer">
        <span class="volume">750ML</span>
        <span class="allergen">CONTAINS SULFATES</span>
      </div>
    </div>
  </section>
</main>
</body>
</html>
```